Brisk Tide needs a web page for E-commerce site

Small startup business looking for a custom website for my New Saltwater apparel Co.

COMPANY OVERVIEW

Brisk Tide was founded In Mont Belvieu, Tx, right on the heart of pelican cove.

Brisk Tide is the adrenaline, sweat pumping moment you find yourself setting the hook on a monster fish. This is the moment when all your senses come to life as you work to land that trophy, and after a grueling fight when your hi-fiving your fishing buddies...It's that moment... when the waters and the air around you are Brisk Sweet....All or Nothing...pure Addiction......This is BRISK TIDE

Looking for a sharp clean sexy web page for my ecommerce page

I like the look of black background websites.

www.brisktidegear.example
Updates

I am using bigcommerce as my host site if that means anything to y'all

Thank you all for the submissions! There were some great ones!  I will have more projects in the future. thanks again

Target Market(s)

inshore/offshore fishing, saltwater enthusiast

Industry/Entity Type

Business

Requirements
Must have
• logo's

inshore/offshore fishing appeal

compatible with bigcommerce site

```html
<!DOCTYPE html>
<html lang="en">
<head>
<meta charset="utf-8">
<title>Brisk Tide – Saltwater Apparel</title>
<link rel="stylesheet" href="https://fonts.googleapis.com/css2?family=Oswald:wght@500;600&family=Ubuntu:wght@400;500;700&display=swap">
<style>
:root{
  --page:#1b1b1b;
  --bar:#2c2c2c;
  --header:#eeeeee;
  --nav-top:#555;
  --nav-bottom:#333;
  --teal:#10a98a;
  --teal-text:#1db896;
  --yellow:#f4e300;
  --card:#3b3b3b;
  --product:#e7e7e7;
  --footer:#333333;
  --footer-base:#2a2a2a;
  --text:#ffffff;
  --ink:#333;
}
*{box-sizing:border-box;margin:0;padding:0}
html,body{width:883px;height:1200px;overflow:hidden}
body{background:var(--page);font-family:"Ubuntu",sans-serif;color:var(--text);position:relative}
.abs{position:absolute}

/* top bar */
.utility-bar{left:0;top:0;width:883px;height:32px;background:var(--bar);border-bottom:2px solid #111}
.utility-bar ul{list-style:none;display:flex;gap:14px;position:absolute;right:76px;top:10px;font-size:10px;color:#eee}
.utility-bar li{display:flex;align-items:center;gap:4px}
.utility-bar svg{width:11px;height:11px;fill:#eee}

/* header */
.site-header{left:0;top:32px;width:883px;height:78px;background:var(--header)}
.brand{left:76px;top:22px;font-size:30px;font-weight:700;color:#1a1a1a;letter-spacing:1px;display:flex;align-items:center;gap:8px}
.brand-dot{width:14px;height:14px;border-radius:50%;background:#1a1a1a}
.phone{right:77px;top:28px;font-size:22px;font-weight:700;color:var(--ink);display:flex;align-items:center;gap:6px}
.phone svg{width:18px;height:20px;fill:var(--ink)}

/* nav */
.main-nav{left:0;top:110px;width:883px;height:40px;background:linear-gradient(var(--nav-top),var(--nav-bottom))}
.main-nav ul{list-style:none;display:flex;position:absolute;left:83px;top:0;height:40px}
.main-nav li{padding:0 12px;line-height:40px;font-size:14px;border-right:1px solid #2a2a2a}
.main-nav li:last-child{border-right:none}
.search{left:564px;top:118px;width:242px;height:27px;background:#2e2e2e;border:1px solid #222;font-size:9px;color:#ddd;padding:7px 8px}
.search svg{position:absolute;right:7px;top:8px;width:10px;height:10px;fill:#888}

/* hero */
.hero{left:77px;top:174px;width:514px;height:239px;background:linear-gradient(180deg,#c9d3d8 0%,#e6ecee 30%,#3fc0b8 52%,#6fd6cc 75%,#b6e9e3 100%)}
.hero-caption{left:0;bottom:0;width:100%;height:49px;background:rgba(220,240,238,.7);color:#333;font-size:14px;padding:15px 22px}
.hero-arrow{top:12px;width:26px;height:26px;border-radius:50%;background:#222}
.hero-arrow svg{width:26px;height:26px}
.sale-panel{left:599px;top:174px;width:207px;height:239px;background:radial-gradient(circle at 50% 30%,#4a4a4a,#262626);text-align:center;font-family:"Oswald",sans-serif}
.sale-title{position:absolute;left:0;width:100%;top:18px;font-size:72px;line-height:80px;color:var(--yellow);font-weight:600}
.sale-off{position:absolute;left:0;width:100%;top:100px;font-size:44px;line-height:48px;font-weight:600}
.sale-for{position:absolute;left:0;width:100%;top:146px;font-size:32px;line-height:36px;font-weight:600}
.buy-now{position:absolute;left:35px;top:189px;width:134px;height:35px;background:var(--teal);font-size:19px;line-height:35px;font-weight:500}

/* categories */
.category{top:428px;width:177px;height:86px;background:var(--card);padding:13px 19px;overflow:hidden}
.category h3{position:relative;z-index:2;font-family:"Oswald",sans-serif;font-weight:500;font-size:16px;color:var(--teal-text);line-height:20px;white-space:nowrap}
.category p{position:relative;z-index:2;font-size:13px;margin-top:4px;white-space:nowrap}
.category .tag{position:relative;z-index:2;display:inline-block;margin-top:7px;background:var(--teal);font-size:9px;padding:3px 7px}
.category .thumb{position:absolute;z-index:1;right:6px;top:10px;width:46px;height:66px;border-radius:6px}

/* section titles */
.section-title{left:76px;font-size:14px;font-weight:500}
.rule{left:77px;width:729px;height:1px;background:#555}
.pager{right:77px;top:535px;display:flex;gap:6px}
.pager svg{width:9px;height:14px;stroke:#eee;stroke-width:2;fill:none}

/* products */
.product{top:570px;width:238px;height:198px;background:var(--product)}
.product .mini-brand{position:absolute;left:10px;top:10px;font-size:11px;font-weight:700;color:#222}
.product .shirt{position:absolute;left:30px;top:26px;width:178px;height:70px;border-radius:8px}
.product .desc{position:absolute;left:0;width:100%;top:126px;text-align:center;font-size:11.5px;color:#555}
.product .price{position:absolute;left:0;width:100%;top:144px;text-align:center;font-size:17px;font-weight:700;color:#333}
.product .price s{font-weight:400;color:#555}
.product .add{position:absolute;left:0;bottom:0;width:100%;height:32px;background:var(--teal);text-align:center;font-size:12px;line-height:32px}
.product .add svg{width:16px;height:16px;vertical-align:-4px;margin-left:3px}

/* brands */
.brand-strip{left:74px;top:832px;width:732px;height:66px;background:#fff;display:flex;justify-content:space-around;align-items:center;padding:0 20px}
.partner{font-size:12px;font-weight:700;color:#2a2a2a;display:flex;align-items:center;gap:5px}
.partner i{width:10px;height:10px;border-radius:50%;background:#2a2a2a;display:block}

/* footer */
.site-footer{left:0;top:945px;width:883px;height:203px;background:var(--footer)}
.footer-col h4{font-size:14px;font-weight:400;color:var(--teal-text)}
.footer-col ul{list-style:none;margin-top:15px}
.footer-col li{font-size:11px;line-height:21.2px;color:#eee}
.newsletter p{font-size:11px;line-height:18px;margin-top:14px;width:170px;text-align:justify}
.field{position:absolute;left:0;width:170px;height:20px;background:#f4f4f4;border:1px solid #ccc;font-size:8px;color:#aaa;padding:4px 10px}
.subscribe{position:absolute;left:95px;top:121px;width:75px;height:18px;border-radius:9px;background:var(--teal);font-size:11px;text-align:center;line-height:18px}
.social{position:absolute;left:0;width:110px;height:20px;display:flex;justify-content:space-between;align-items:center;font-size:11px}
.social i{width:20px;height:20px;border-radius:50%;background:#fff;display:block}
.cards{position:absolute;left:-11px;top:130px;display:flex;gap:2px}
.cards span{width:30px;height:18px;background:#f2f2f2;border-radius:2px;font-size:6.5px;color:#333;text-align:center;line-height:18px}
.footer-base{left:0;top:1148px;width:883px;height:52px;background:var(--footer-base);font-size:11px;text-align:center;line-height:50px;color:#eee}
</style>
</head>
<body>

<div class="abs utility-bar">
  <ul>
    <li><svg viewBox="0 0 10 10"><circle cx="5" cy="3" r="2.5"/><path d="M0 10c0-3 2-4.5 5-4.5s5 1.5 5 4.5z"/></svg>My Account</li>
    <li><svg viewBox="0 0 10 10"><rect x="1" y="1" width="8" height="6" rx="1"/><circle cx="3" cy="8.5" r="1.2"/><circle cx="7" cy="8.5" r="1.2"/></svg>Order Status</li>
    <li><svg viewBox="0 0 10 10"><path d="M2 0h5l2 2v8H2z"/></svg>Wish Lists</li>
    <li><svg viewBox="0 0 10 10"><rect x="1" y="3" width="8" height="7"/><rect x="0" y="2" width="10" height="2"/></svg>Gift Certificates</li>
    <li><svg viewBox="0 0 10 10"><path d="M0 2h10l-1.5 6h-7z"/></svg>View Cart</li>
    <li><svg viewBox="0 0 10 10"><rect x="1" y="4" width="8" height="6"/><path d="M3 4V2.5a2 2 0 014 0V4" stroke="#eee" fill="none"/></svg>Sign in</li>
  </ul>
</div>

<header class="abs site-header">
  <div class="abs brand"><span class="brand-dot"></span>BRISK TIDE</div>
  <div class="abs phone"><svg viewBox="0 0 18 20"><path d="M4 1l3 4-2 2c1 3 3 5 6 7l2-2 4 3-2 4C7 18 1 11 1 3z"/></svg>1-800-555-0142</div>
</header>

<nav class="abs main-nav">
  <ul><li>Shop</li><li>Support</li><li>Connect</li><li>Find</li><li>Sale</li><li>Great Deals</li></ul>
</nav>
<div class="abs search">Type search<svg viewBox="0 0 10 10"><circle cx="4" cy="4" r="3" stroke="#888" stroke-width="1.5" fill="none"/><path d="M6 6l3.5 3.5" stroke="#888" stroke-width="1.5"/></svg></div>

<section class="abs hero" role="img" aria-label="Photo of an angler casting a rod over turquoise sea under a cloudy sky">
  <div class="abs hero-caption">Great Apparels &amp; Great Offers
    <span class="abs hero-arrow" style="left:436px"><svg viewBox="0 0 26 26"><path d="M15 7l-6 6 6 6" stroke="#fff" stroke-width="3" fill="none"/></svg></span>
    <span class="abs hero-arrow" style="left:468px"><svg viewBox="0 0 26 26"><path d="M11 7l6 6-6 6" stroke="#fff" stroke-width="3" fill="none"/></svg></span>
  </div>
</section>

<aside class="abs sale-panel">
  <div class="sale-title">SALE</div>
  <div class="sale-off">70% OFF</div>
  <div class="sale-for">FOR FISHING</div>
  <div class="buy-now">BUY NOW</div>
</aside>

<div class="abs category" style="left:76px"><h3>FISHING BOOTS</h3><p>Men &amp; Women</p><span class="tag">New Deals</span><span class="thumb" role="img" aria-label="Wading boot" style="background:linear-gradient(#8a8470,#4a473c)"></span></div>
<div class="abs category" style="left:261px"><h3>WADERS</h3><p>Men &amp; Women</p><span class="tag">New Deals</span><span class="thumb" role="img" aria-label="Chest waders" style="background:linear-gradient(#6a6560,#2f2d2b)"></span></div>
<div class="abs category" style="left:444px"><h3>OUTWEAR</h3><p>Men &amp; Women</p><span class="tag">New Deals</span><span class="thumb" role="img" aria-label="Hooded rain jacket" style="background:linear-gradient(#d9d7c4,#a9a68f)"></span></div>
<div class="abs category" style="left:629px"><h3>HEADWEAR</h3><p>Men &amp; Women</p><span class="tag">New Deals</span><span class="thumb" role="img" aria-label="Fishing cap" style="background:linear-gradient(#ddd8c8,#a8a291)"></span></div>

<h2 class="abs section-title" style="top:531px">Featured Products</h2>
<div class="abs pager"><svg viewBox="0 0 9 14"><path d="M7 2L2 7l5 5"/></svg><svg viewBox="0 0 9 14"><path d="M2 2l5 5-5 5"/></svg></div>
<div class="abs rule" style="top:557px"></div>

<article class="abs product" style="left:77px">
  <span class="mini-brand">BRISK TIDE</span>
  <span class="shirt" role="img" aria-label="White t-shirt front and back with teal fish print" style="background:linear-gradient(90deg,#ffffff,#d5ebe8,#ffffff)"></span>
  <p class="desc">Ut dignissim, ante at gravida dapibus</p>
  <p class="price">$65.69 <s>$75.00</s></p>
  <div class="add">Add to Cart<svg viewBox="0 0 16 16"><circle cx="8" cy="8" r="8" fill="#fff"/><path d="M6 4l4 4-4 4" stroke="#10a98a" stroke-width="2.2" fill="none"/></svg></div>
</article>
<article class="abs product" style="left:321px">
  <span class="mini-brand">BRISK TIDE</span>
  <span class="shirt" role="img" aria-label="Yellow t-shirt front and back with blue marlin print" style="background:linear-gradient(90deg,#f4ec8e,#eee58a,#f4ec8e)"></span>
  <p class="desc">Ut dignissim, ante at gravida dapibus</p>
  <p class="price">$65.69 <s>$75.00</s></p>
  <div class="add">Add to Cart<svg viewBox="0 0 16 16"><circle cx="8" cy="8" r="8" fill="#fff"/><path d="M6 4l4 4-4 4" stroke="#10a98a" stroke-width="2.2" fill="none"/></svg></div>
</article>
<article class="abs product" style="left:568px">
  <span class="mini-brand">BRISK TIDE</span>
  <span class="shirt" role="img" aria-label="Dark brown t-shirt front and back with white print" style="background:linear-gradient(90deg,#2a241c,#3a3126,#2a241c)"></span>
  <p class="desc">Ut dignissim, ante at gravida dapibus</p>
  <p class="price">$65.69 <s>$75.00</s></p>
  <div class="add">Add to Cart<svg viewBox="0 0 16 16"><circle cx="8" cy="8" r="8" fill="#fff"/><path d="M6 4l4 4-4 4" stroke="#10a98a" stroke-width="2.2" fill="none"/></svg></div>
</article>

<h2 class="abs section-title" style="top:790px">Featured Brands</h2>
<div class="abs rule" style="top:817px"></div>
<div class="abs brand-strip">
  <span class="partner"><i></i>MARLOWE</span>
  <span class="partner">NORTHREEL</span>
  <span class="partner"><i></i>BAYCREST</span>
  <span class="partner">KEELSON</span>
  <span class="partner">LINEWEAVE</span>
  <span class="partner"><i></i>SONARIX</span>
</div>

<footer class="abs site-footer">
  <div class="abs footer-col" style="left:77px;top:25px"><h4>Quick Links</h4>
    <ul><li>Home</li><li>Shop</li><li>Support</li><li>Connect</li><li>Find</li><li>Sale</li><li>Great Deals</li></ul></div>
  <div class="abs footer-col" style="left:262px;top:25px"><h4>Support Links</h4>
    <ul style="margin-top:16px"><li style="line-height:18.5px">Legal Notice</li><li style="line-height:18.5px">Privacy Policy</li><li style="line-height:18.5px">Terms &amp; Conditions</li><li style="line-height:18.5px">Help</li></ul></div>
  <div class="abs footer-col newsletter" style="left:448px;top:25px;width:170px;height:150px"><h4>Newsletter SignUp</h4>
    <p>Sign-up for our daily emails by entering your information below:</p>
    <div class="field" style="top:68px">Name</div>
    <div class="field" style="top:100px">Enter Your E-Mail ID</div>
    <div class="subscribe">Subscribe</div></div>
  <div class="abs footer-col" style="left:693px;top:25px;width:113px;height:160px"><h4>Connect With Us</h4>
    <div class="social" style="top:30px"><i></i>Chirper</div>
    <div class="social" style="top:59px"><i></i>Friendbook</div>
    <div class="social" style="top:87px"><i></i>WorkLink</div>
    <div class="cards"><span>PayCo</span><span>CardX</span><span>NetPay</span><span>Cashly</span></div></div>
</footer>
<div class="abs footer-base">Copyright ©2013 Company Name &nbsp;&nbsp; - All rights reserved</div>

</body>
</html>
```